VELTO SMS Web Design Project

We need a new web design to replace the current one. See the current one: http://www.sms.tarvold.org/tarvold

The new name instead of Quillet Communications is changed to Velto SMS

Make provisions for were members can advertise their products / business.

```html
<!DOCTYPE html>
<html lang="en">
<head>
<meta charset="utf-8">
<title>Velto SMS — Your Partner to reach the world</title>
<link href="https://fonts.googleapis.com/css2?family=Source+Sans+3:wght@400;600&family=Arimo:wght@400;700&display=swap" rel="stylesheet">
<style>
  :root {
    --blue: #1a4f8f;
    --blue-dark: #0f3b73;
    --nav-blue: #1c4e8c;
    --red: #c8161d;
    --text: #3b3b3b;
    --muted: #666;
    --page: #f2f2f3;
    --panel: #ffffff;
    --line: #cfcfd3;
    --grey-dot: #8a8a8a;
  }
  * { box-sizing: border-box; margin: 0; padding: 0; }
  html, body { width: 924px; height: 1200px; overflow: hidden; }
  body {
    position: relative;
    background: var(--page);
    font-family: "Source Sans 3", sans-serif;
    color: var(--text);
  }
  .abs { position: absolute; }

  /* Header */
  .brand-device { left: 26px; top: 5px; width: 85px; height: 78px; border-radius: 10px;
    background: linear-gradient(135deg, #9aa0a8, #2b2e33); transform: rotate(-18deg) scale(.78); }
  .brand-name { left: 115px; top: 24px; font-size: 36px; color: var(--blue); font-weight: 400; letter-spacing: .2px; }
  .partner { left: 485px; top: 20px; display: flex; align-items: center; gap: 8px; }
  .partner .dot { width: 34px; height: 34px; border-radius: 50%; background: #2f6e8f; }
  .partner span { font-size: 17px; color: #3a3a3a; }
  .search { left: 719px; top: 33px; width: 174px; height: 23px; background: #fff;
    border: 1px solid #d0d0d0; box-shadow: 0 1px 2px rgba(0,0,0,.12);
    font: italic 10px "Arimo", sans-serif; color: #aaa; padding: 5px 12px; }
  .search svg { position: absolute; right: 6px; top: 6px; }

  /* Navigation */
  .nav { left: 25px; top: 87px; width: 871px; height: 40px; display: flex;
    background: var(--nav-blue); border-radius: 2px; }
  .nav a { display: flex; align-items: center; justify-content: center; color: #fff;
    text-decoration: none; font-size: 13.5px; border-right: 1px solid #4e77a9; }
  .nav a:last-child { border-right: 0; }
  .nav a.active { background: var(--red); }

  /* Hero */
  .hero-photo { left: 25px; top: 138px; width: 471px; height: 269px;
    background: linear-gradient(180deg, #9fb69a 0%, #c6cfc0 40%, #7fa05a 100%); }
  .hero-side { left: 496px; top: 138px; width: 397px; height: 269px;
    background: linear-gradient(90deg, #f4f4f5, #fbfbfb); }
  .hero-band { left: 503px; top: 212px; width: 368px; height: 86px; text-align: center;
    background: linear-gradient(90deg, #e6e6e8, #f5f5f6 70%, #fafafa); }
  .hero-band h1 { font-size: 29px; font-weight: 400; color: #3a5a9e; margin-top: 10px; }
  .hero-band p { font-size: 17px; color: #333; margin-top: 4px; }
  .hero-dots { left: 500px; top: 367px; width: 376px; height: 14px; }
  .hero-shadow { left: 70px; top: 410px; width: 760px; height: 8px; border-radius: 50%;
    background: radial-gradient(ellipse at center, rgba(0,0,0,.45), rgba(0,0,0,0) 70%); }

  /* Left column */
  .box { background: var(--panel); border: 1px solid #d6d6d8; border-radius: 4px; }
  .logon { left: 26px; top: 446px; width: 219px; height: 158px; }
  .logon-head { height: 33px; border-bottom: 1px solid #e0e0e0; display: flex; align-items: center;
    padding-left: 10px; gap: 12px; font-size: 13.5px; color: var(--blue-dark); font-weight: 600;
    background: linear-gradient(#fff, #f1f1f1); border-radius: 4px 4px 0 0; }
  .field { position: absolute; left: 0; font: 9.5px "Arimo", sans-serif; color: #666; }
  .field label { position: absolute; right: 0; width: 70px; text-align: right; }
  .field input { position: absolute; left: 84px; width: 117px; height: 21px; border: 1px solid #aaa;
    background: linear-gradient(#e4e4e4, #f3f3f3); }
  .submit { position: absolute; left: 87px; top: 118px; width: 64px; height: 22px; background: var(--blue-dark);
    color: #fff; font: 11.5px "Arimo", sans-serif; display: flex; align-items: center; justify-content: center; }
  .signup-btn { left: 26px; top: 615px; width: 219px; height: 47px; border-radius: 3px;
    background: linear-gradient(#2c5b9b, #133f7a); color: #fff; font-size: 19px;
    display: flex; align-items: center; padding-left: 46px; }
  .signup-btn svg { position: absolute; left: 10px; top: 9px; }
  .promo { left: 28px; top: 676px; width: 222px; height: 192px; border-radius: 6px; border: 2px solid #d5d5d7;
    background: linear-gradient(90deg, #cfcfd3 0%, #dcdcdf 45%, #c8b79b 75%, #e2d8c6 100%); overflow: hidden; }
  .promo p { position: absolute; left: 9px; top: 46px; font: 14px "Arimo", sans-serif; color: #222; line-height: 19px; }
  .promo p b { color: #2466b2; }
  .promo .click { position: absolute; left: 9px; top: 116px; width: 94px; height: 18px; border-radius: 9px;
    background: linear-gradient(#fff, #dcdcdc); border: 1px solid #b8b8b8; font: italic 11px "Arimo", sans-serif;
    color: #777; text-align: center; line-height: 16px; }
  .feature { left: 26px; top: 884px; width: 219px; height: 192px; }
  .feature-head { height: 33px; border-bottom: 1px solid #e0e0e0; padding: 6px 0 0 20px; font-size: 16.5px;
    color: var(--blue); background: linear-gradient(#fff, #f1f1f1); border-radius: 4px 4px 0 0; }
  .feature-item { position: absolute; left: 12px; width: 200px; font: 10px/15px "Arimo", sans-serif; color: #444; }
  .feature-item .icon { position: absolute; left: 0; top: 0; width: 50px; height: 50px; }
  .feature-item p { margin-left: 60px; }
  .more { font: 10px "Arimo", sans-serif; color: var(--red); text-decoration: none; }
  .feature-item .more { display: block; text-align: right; padding-right: 6px; margin-top: 3px; }

  /* Headings */
  .heading { font-size: 20px; font-weight: 400; color: var(--blue); padding-bottom: 5px;
    border-bottom: 1.5px dotted #777; }

  /* Welcome */
  .welcome { left: 284px; top: 452px; width: 214px; }
  .welcome span { color: var(--red); }
  .welcome-photo { left: 287px; top: 495px; width: 254px; height: 133px; border: 3px solid #fff;
    box-shadow: 0 0 2px rgba(0,0,0,.25);
    background: linear-gradient(90deg, #8f94a0 0%, #c7c9d0 35%, #5b4a6d 55%, #d2d4da 80%, #9aa0ab 100%); }
  .welcome-text { left: 284px; top: 643px; width: 330px; font-size: 11px; line-height: 16.6px; color: #444; }

  /* News */
  .news-divider { left: 628px; top: 452px; width: 1px; height: 320px;
    background: linear-gradient(#fff0, #d9d9db 30%, #d9d9db 70%, #fff0); }
  .news { left: 658px; top: 452px; width: 220px; }
  .news-item { position: absolute; left: 658px; width: 250px; font: 10px/15px "Arimo", sans-serif; color: #444; }
  .news-item time { display: block; margin-bottom: 7px; }

  /* Services */
  .services { left: 287px; top: 767px; width: 546px; }
  .service { position: absolute; top: 823px; width: 200px; }
  .service .num { position: absolute; left: 0; top: 2px; font-size: 56px; color: #a8a8a8; line-height: 1; font-weight: 300; }
  .service h3 { margin-left: 24px; font-size: 14.5px; font-weight: 400; color: #2a66b0; padding-bottom: 6px;
    border-bottom: 1px solid #ccc; width: 159px; }
  .service p { margin: 6px 0 0 24px; width: 166px; font: 10px/15px "Arimo", sans-serif; color: #444; }

  /* Testimonials */
  .testimonials { left: 287px; top: 942px; width: 546px; }
  .quote { left: 287px; top: 994px; width: 617px; font: 10.6px/18.5px "Arimo", sans-serif; color: #555; text-indent: 16px; }
  .quote .mark { font-family: Georgia, serif; font-size: 15px; color: #888; }
  .author { left: 700px; top: 1062px; width: 164px; text-align: right; font: 12px "Arimo", sans-serif; color: #555; }

  /* Footer */
  .footer { left: 0; top: 1108px; width: 924px; height: 92px; background: #f7f7f8; border-top: 2px solid #c9c9cc; }
  .social { right: 32px; top: 1126px; display: flex; gap: 11px; }
  .social span { width: 24px; height: 24px; border-radius: 3px; background: var(--nav-blue); }
  .copyright { right: 29px; top: 1165px; font: 11.5px "Arimo", sans-serif; color: #333; }
</style>
</head>
<body>

<header>
  <div class="abs brand-device" role="img" aria-label="Photo of a slider mobile phone"></div>
  <div class="abs brand-name">Velto SMS</div>
  <div class="abs partner"><div class="dot"></div><span>Lumen Fellowship</span></div>
  <div class="abs search">Search Product
    <svg width="10" height="10" viewBox="0 0 10 10"><circle cx="4" cy="4" r="3" fill="none" stroke="#aaa" stroke-width="1.2"/><line x1="6.2" y1="6.2" x2="9" y2="9" stroke="#aaa" stroke-width="1.4"/></svg>
  </div>
</header>

<nav class="abs nav">
  <a class="active" style="width:79px">Home</a>
  <a style="width:101px">About Us</a>
  <a style="width:152px">Product &amp; Services</a>
  <a style="width:83px">Pricing</a>
  <a style="width:103px">Client Login</a>
  <a style="width:95px">Sign Up</a>
  <a style="width:69px">FAQ</a>
  <a style="width:189px">Contact Us</a>
</nav>

<section class="hero">
  <div class="abs hero-photo" role="img" aria-label="Photo of a smiling young man in a cap texting on his phone in a park"></div>
  <div class="abs hero-side"></div>
  <div class="abs hero-band">
    <h1>Velto SMS</h1>
    <p>Your Partner to reach the world</p>
  </div>
  <svg class="abs hero-dots" viewBox="0 0 376 14">
    <line x1="0" y1="7" x2="60" y2="7" stroke="#d4d4d6"/>
    <line x1="240" y1="7" x2="376" y2="7" stroke="#d4d4d6"/>
    <circle cx="77" cy="7" r="6" fill="#8a8a8a"/>
    <circle cx="108" cy="7" r="6" fill="#c8161d"/>
    <circle cx="139" cy="7" r="6" fill="#8a8a8a"/>
    <circle cx="170" cy="7" r="6" fill="#8a8a8a"/>
    <circle cx="201" cy="7" r="6" fill="#8a8a8a"/>
  </svg>
  <div class="abs hero-shadow"></div>
</section>

<aside>
  <div class="abs box logon">
    <div class="logon-head">
      <svg width="24" height="24" viewBox="0 0 24 24"><circle cx="12" cy="8" r="5" fill="#444"/><path d="M2 24c0-7 4-10 10-10s10 3 10 10z" fill="#333"/></svg>
      LOGON
    </div>
    <div class="field" style="top:55px;width:219px"><label style="left:0;width:76px">User Name :</label><input style="top:-5px"></div>
    <div class="field" style="top:90px;width:219px"><label style="left:0;width:76px">Password :</label><input style="top:-4px"></div>
    <div class="submit">Submit</div>
  </div>

  <div class="abs signup-btn">
    <svg width="28" height="30" viewBox="0 0 28 30"><path d="M7 13V9a7 7 0 0 1 14 0v4" fill="none" stroke="#c9ccd2" stroke-width="3"/><rect x="3" y="13" width="22" height="16" rx="2" fill="#e1b23a"/></svg>
    Velto SMS Sign Up
  </div>

  <div class="abs promo" role="img" aria-label="Photo of a smiling woman holding a mobile phone">
    <p>Send SMS and get<br><b>negotiable discounts<br>also</b>.</p>
    <div class="click">Click here</div>
  </div>

  <div class="abs box feature">
    <div class="feature-head">Feature Product</div>
    <div class="feature-item" style="top:50px">
      <div class="icon" role="img" aria-label="Illustration of a blue mail envelope icon" style="border-radius:50%;background:radial-gradient(circle at 40% 35%,#6fa4e0,#1d4f9a)"></div>
      <p>Nunc varius facilisis eros. Sed erat. In in velit quis arcu ornare laoreet.</p>
      <a class="more">View More &nbsp;&gt;&gt;</a>
    </div>
    <div class="feature-item" style="top:129px">
      <div class="icon" role="img" aria-label="Illustration of blue envelopes with a gear" style="background:linear-gradient(135deg,#3b7ac4,#9aa4b0)"></div>
      <p style="margin-left:64px">Nunc varius facilisis eros. Sed erat. In in velit quis arcu ornare laoreet.</p>
      <a class="more">View More &nbsp;&gt;&gt;</a>
    </div>
  </div>
</aside>

<main>
  <h2 class="abs heading welcome">Welcome to Velto <span>SMS</span></h2>
  <div class="abs welcome-photo" role="img" aria-label="Photo of a young couple checking their phones in a shop"></div>
  <p class="abs welcome-text">SMS messaging is one of the fastest growing communication formats in Nigeria. Companies, clubs, institutions, religious organizations and individuals have discovered the power of contacting clients and friends quickly and economically through the power of SMS messages to cell phones for information on events and celebrations.</p>

  <div class="abs news-divider"></div>
  <h2 class="abs heading news">Latest News</h2>
  <article class="news-item" style="top:495px"><time>June 20, 2012</time>Nunc varius facilisis eros. Sed erat. In in velit quis arcu ornare laoreet. Nunc varius facilisis eros. Sed erat. In in velit quis arcu ornare laoreet.</article>
  <article class="news-item" style="top:579px"><time>June 20, 2012</time>Nunc varius facilisis eros. Sed erat. In in velit quis arcu ornare laoreet. Nunc varius facilisis eros. Sed erat. In in velit quis arcu ornare laoreet.</article>
  <article class="news-item" style="top:663px"><time>June 20, 2012</time>Nunc varius facilisis eros. Sed erat. In in velit quis arcu ornare laoreet. Nunc varius facilisis eros. Sed erat. In in velit quis arcu ornare laoreet.</article>
  <a class="abs more" style="left:660px;top:745px">View More &nbsp;&gt;&gt;</a>

  <h2 class="abs heading services">Our Services</h2>
  <div class="service" style="left:287px"><span class="num">1</span><h3>SEND ALL YOUR SMS</h3><p>Pellentesque elementum dolor suscipit feugiat augue vitae turpis viverra id adipiscing lorem tincidunt.</p></div>
  <div class="service" style="left:492px"><span class="num">2</span><h3>SEND BULK SMS</h3><p>Pellentesque elementum dolor suscipit feugiat augue vitae turpis viverra id adipiscing lorem tincidunt.</p></div>
  <div class="service" style="left:710px"><span class="num">3</span><h3 style="margin-left:38px;width:170px">RESELLER OF BULK SMS</h3><p style="margin-left:38px;width:170px">Pellentesque elementum dolor suscipit feugiat augue vitae turpis viverra id adipiscing lorem tincidunt.</p></div>

  <h2 class="abs heading testimonials">Client’s Testimonials</h2>
  <blockquote class="abs quote"><span class="mark">“</span> Neque porro quisquam est, qui dolorem ipsum quia dolor sit amet, consectetur, adipisci velit, sed quia non numquam eius modi tempora incidunt ut labore et dolore magnam aliquam quaerat voluptatem. Ut enim ad minima veniam, quis nostrum exercitationem ullam corporis suscipit laboriosam nisi ut aliquid ex ea commodi consequatur. <span class="mark">”</span></blockquote>
  <div class="abs author">- Marcus Hale</div>
</main>

<footer>
  <div class="abs footer"></div>
  <div class="abs social" aria-label="Social links"><span></span><span></span><span></span><span></span></div>
  <div class="abs copyright">Copyright © 2012 Velto SMS, All rights reserved</div>
</footer>

</body>
</html>
```